New company looking for logo, for business cards and email signature.
we provide Safety, Training and Project Management Services to Mining and Transport sectors.

Industry/Entity Type

Business

Contact Information for Business Card

HARTWELL CONSULTANCY, Owen Fairclough, Principal Consultant, 0491362847, hartwellconsultancy@postvane.com , Unit 214,Corvale Business Hub,517 Tindal Road, Mackay, 4750.
Sustainable Production through Safety, Training and Leadership.

```html
<!DOCTYPE html>
<html lang="en">
<head>
<meta charset="utf-8">
<title>Hartwell Consultancy – Business Card</title>
<link rel="stylesheet" href="https://fonts.googleapis.com/css2?family=Ubuntu:ital,wght@0,400;0,500;0,700;1,700&display=swap">
<style>
  :root {
    --backdrop: #1e1e20;
    --card-white: #f7f7f7;
    --brand-blue: #1d5f95;
    --blue-deep: #0f5f9c;
    --blue-mid: #1878b4;
    --blue-light: #2b86ad;
    --accent-cyan: #1ec8f0;
    --text-light: #ffffff;
    --text-soft: #e6f1f8;
  }
  * { box-sizing: border-box; margin: 0; padding: 0; }
  html, body {
    width: 1200px; height: 1000px; overflow: hidden;
    background: var(--backdrop);
    font-family: "Ubuntu", sans-serif;
  }
  .sheet {
    width: 1200px; height: 1000px;
    display: flex; flex-direction: column;
    align-items: center; justify-content: center;
    gap: 60px;
  }
  .card {
    width: 640px; height: 390px;
    position: relative; overflow: hidden;
    box-shadow: 0 12px 30px rgba(0,0,0,.5);
  }

  /* Back side */
  .card-back {
    background: linear-gradient(160deg, var(--blue-deep) 0%, var(--blue-mid) 50%, var(--blue-light) 100%);
    display: flex; align-items: center; justify-content: center;
  }
  .wordmark { text-align: center; font-weight: 700; line-height: 1; }
  .wordmark-name { font-size: 58px; letter-spacing: 1px; }
  .wordmark-sub { font-size: 17px; letter-spacing: 4px; margin-top: 8px; }
  .card-back .wordmark { color: var(--text-light); }

  /* Front side */
  .card-front { display: flex; }
  .front-brand {
    width: 38%; background: var(--card-white);
    display: flex; align-items: center; justify-content: center;
  }
  .front-brand .wordmark { color: var(--brand-blue); }
  .front-brand .wordmark-name { font-size: 38px; }
  .front-brand .wordmark-sub { font-size: 11px; letter-spacing: 3px; margin-top: 6px; }
  .front-details {
    flex: 1;
    background: linear-gradient(165deg, var(--blue-deep) 0%, var(--blue-mid) 55%, var(--blue-light) 100%);
    color: var(--text-soft);
    padding: 34px 26px 0 34px;
    position: relative;
  }
  .holder { position: relative; padding-left: 0; }
  .holder::before {
    content: ""; position: absolute; left: -20px; top: 2px;
    width: 5px; height: 26px; background: var(--accent-cyan);
  }
  .holder-name {
    font-size: 21px; font-weight: 700; font-style: italic;
    color: var(--text-light); letter-spacing: .5px;
  }
  .holder-role { font-size: 16px; margin-top: 2px; }
  .contact { list-style: none; margin-top: 82px; font-size: 15.5px; line-height: 1.55; }
</style>
</head>
<body>
<main class="sheet">
  <section class="card card-back" aria-label="Card back">
    <div class="wordmark">
      <div class="wordmark-name">HARTWELL</div>
      <div class="wordmark-sub">CONSULTANCY</div>
    </div>
  </section>

  <section class="card card-front" aria-label="Card front">
    <div class="front-brand">
      <div class="wordmark">
        <div class="wordmark-name">HARTWELL</div>
        <div class="wordmark-sub">CONSULTANCY</div>
      </div>
    </div>
    <div class="front-details">
      <div class="holder">
        <p class="holder-name">OWEN FAIRCLOUGH</p>
        <p class="holder-role">principal consultant</p>
      </div>
      <ul class="contact">
        <li>Unit 214,Corvale Business Hub</li>
        <li>517 Tindal Road, Mackay, 4750</li>
        <li>p : 0491362847</li>
        <li>e : hartwellconsultancy@postvane.com</li>
      </ul>
    </div>
  </section>
</main>
</body>
</html>
```